Business Card Design for Pastor/Church Leadership - simple, elegant, "different"

Design a name card based on logo and color from our branding guide - see file "MBF Logo and Color".
The teal frame around the logo is not part of the logo and is a not necessary design element for the name card (as the attached PDF file may suggest).
The font suggested by branding is "Frutiger 55 Roman".
The file "not good.pdf", a sample of a name card that is NOT good.
- fonts too small to read
- the tagline on the logo "Still waters, open door" not easy to read with logo used in this design
- "MAPLE GROVE FELLOWSHIP" unnecessarily duplicated - possibly because logo too small
- not sure about the green frame, probably better to drop

Target Market(s)

broad, all people the pastor of an international church in Tokyo meets

Industry/Entity Type

Business

Contact Information for Business Card

Mattias R. Pellworth
Pastor
3-9-4 Kawaranodai, Hinokawa-ku
Tokyo 168-0412 (Church)
2-21 Ochibamachi, Hinokawa-ku
Tokyo 168-0427 (Home)
Tel: 03-5817-2963
E-mail: pastor@maplegrovefell.org
URL: http://www.maplegrovefell.org

Font styles to use
Sans Serif
Other font styles liked:
• Frutiger 55 Roman (want, not must)

Requirements
Must have
• must include logo
• must make use of the "bright turquoise color"
• Cyan = 59, Magenta = 0, Yellow=24, Black=0
• Red=3.1%, Green=91%, Blue=87.1%
• Key Info (name) must be easy to read (see notes on bad sample namecard attached)

```html
<!DOCTYPE html>
<html lang="en">
<head>
<meta charset="utf-8">
<title>Maple Grove Fellowship – Pastor Business Card</title>
<link rel="stylesheet" href="https://fonts.googleapis.com/css2?family=Open+Sans:wght@400;700&display=swap">
<style>
  :root {
    --teal: #5bc5c8;
    --white: #ffffff;
    --backdrop: #8a939c;
    --card-shadow: rgba(0, 0, 0, 0.25);
  }
  * { margin: 0; padding: 0; box-sizing: border-box; }
  html, body {
    width: 1200px;
    height: 833px;
    overflow: hidden;
    background: var(--backdrop);
    font-family: "Open Sans", sans-serif;
  }
  .canvas {
    width: 1200px;
    height: 833px;
    display: flex;
    align-items: center;
    justify-content: center;
  }
  .business-card {
    width: 1000px;
    height: 606px;
    display: flex;
    box-shadow: 0 10px 30px var(--card-shadow);
  }
  .brand-side {
    width: 440px;
    background: var(--white);
    display: flex;
    flex-direction: column;
    align-items: center;
    justify-content: center;
    color: var(--teal);
  }
  .brand-mark {
    width: 110px;
    height: 110px;
    background: var(--teal);
    margin-bottom: 38px;
  }
  .brand-name {
    font-size: 22px;
    font-weight: 400;
    letter-spacing: 2.5px;
    text-transform: uppercase;
    white-space: nowrap;
  }
  .brand-rule {
    width: 340px;
    height: 3px;
    background: var(--teal);
    margin: 12px 0 14px;
  }
  .brand-tagline {
    font-size: 22px;
    font-weight: 400;
    letter-spacing: 1.5px;
    white-space: nowrap;
  }
  .contact-side {
    flex: 1;
    background: var(--teal);
    color: var(--white);
    padding: 92px 0 0 66px;
  }
  .contact-name {
    font-size: 38px;
    font-weight: 700;
    line-height: 1.1;
    white-space: nowrap;
  }
  .contact-role {
    font-size: 22px;
    font-weight: 400;
    margin-bottom: 30px;
  }
  .contact-address,
  .contact-lines {
    font-size: 23px;
    font-weight: 400;
    line-height: 1.35;
    font-style: normal;
    white-space: nowrap;
  }
  .contact-address { margin-bottom: 44px; }
</style>
</head>
<body>
  <main class="canvas">
    <article class="business-card">
      <section class="brand-side">
        <div class="brand-mark" aria-hidden="true"></div>
        <p class="brand-name">Maple Grove Fellowship</p>
        <div class="brand-rule"></div>
        <p class="brand-tagline">Still waters, open door</p>
      </section>
      <section class="contact-side">
        <h1 class="contact-name">Mattias R. Pellworth</h1>
        <p class="contact-role">Pastor</p>
        <address class="contact-address">
          3-9-4 Kawaranodai, Hinokawa-ku<br>
          Tokyo 168-0412 (Church)<br>
          2-21 Ochibamachi, Hinokawa-ku<br>
          Tokyo 168-0427 (Home)
        </address>
        <p class="contact-lines">
          Tel: 03-5817-2963<br>
          E-mail: pastor@maplegrovefell.org
        </p>
      </section>
    </article>
  </main>
</body>
</html>
```